Pre-drywall Construction postcard mailer

Need a 2-sided postcard to be mailed to real estate agents advertising Pre-drywall Inspections, 5.5 X 8.5 oversized postcard with $25 off the inspection fee. Velkor Solutions is a home inspection company in Atlanta.

Key words: "New Construction is on the Rise! Velkor Inspectors are BTW (code) certified and Fully Insured. Protect your clients with a Pre-drywall inspection."
" $25 coupon for your next Pre-drywall inspection. Mention coupon when booking the Inspection. "
Include a phrase that says, "Once the drywall is hung, hidden problems cannot be seen." Tim Garrowby, Owner Velkor

555.218.0736 www.the Velkor path.example

Colors: dark green, aqua, lite greens (Go to website to see colors)

Target Market(s)

Real estate agents in SE United States

Industry/Entity Type

Home Inspection

Requirements
Must have
• Our logo (See website) and everything that is in the Task Description. Large one on front and small one by return address.
• Return address for mailer side: 2917 Pelham Row, Suite 340 Buford, GA 30299
• Company name: Dwelling Examiners of Norvale, dba Velkor Solutions
• Ph. # 555.218.0736 www.theVelkorpath.example
• Hours: M - F 8:00AM-8PM Sat. 10AM-2PM
• Need illustration of a home under construction-framework only

```html
<!DOCTYPE html>
<html lang="en">
<head>
<meta charset="utf-8">
<title>Pre-drywall Inspection Postcard</title>
<link href="https://fonts.googleapis.com/css2?family=Audiowide&family=Ubuntu:wght@400;500;700&display=swap" rel="stylesheet">
<style>
  :root {
    --page-bg: #e9e9e9;
    --card-bg: #ffffff;
    --brand-green: #6aac45;
    --brand-green-dark: #4f8f30;
    --ink: #1d1d1d;
    --muted-ink: #2a2a2a;
    --aqua: #2a9fb5;
    --illus-light: #f2f2f2;
    --illus-mid: #d9d9d9;
    --illus-wood: #b5651d;
  }
  * { box-sizing: border-box; margin: 0; padding: 0; }
  html, body {
    width: 1200px; height: 900px; overflow: hidden;
    background: var(--page-bg);
  }
  .postcard {
    position: absolute;
    left: 322px; top: 20px;
    width: 556px; height: 860px;
    background: var(--card-bg);
    box-shadow: 0 4px 14px rgba(0,0,0,0.25);
    overflow: hidden;
    font-family: "Ubuntu", sans-serif;
    color: var(--ink);
  }
  .headline {
    font-family: "Audiowide", sans-serif;
    color: var(--brand-green);
    text-align: center;
    font-size: 37px;
    line-height: 46px;
    padding-top: 20px;
    letter-spacing: 0.5px;
  }
  .illustration {
    position: absolute;
    left: 0; top: 116px;
    width: 556px; height: 420px;
    background: radial-gradient(ellipse at 55% 50%, var(--illus-light) 0%, var(--illus-mid) 70%, #cfcfcf 100%);
  }
  .illustration-frame {
    position: absolute;
    left: 180px; top: 60px;
    width: 240px; height: 230px;
    background: linear-gradient(160deg, rgba(181,101,29,0.35), rgba(210,180,140,0.35));
    border-radius: 6px;
  }
  .swoosh {
    position: absolute;
    left: 0; top: 470px;
    width: 556px; height: 80px;
  }
  .tagline {
    position: absolute;
    top: 556px; left: 0; width: 100%;
    text-align: center;
    font-size: 23px;
    line-height: 28px;
    font-weight: 500;
  }
  .credentials {
    position: absolute;
    top: 625px; left: 0; width: 100%;
    text-align: center;
    font-size: 13.5px;
    line-height: 20px;
    font-weight: 700;
    color: var(--muted-ink);
  }
  .contact-row {
    position: absolute;
    top: 688px; left: 36px;
    display: flex; align-items: center;
  }
  .brand-mark {
    display: flex; align-items: center;
    margin-right: 24px;
  }
  .brand-dot {
    width: 22px; height: 22px; border-radius: 50%;
    background: var(--aqua);
    margin-right: 8px;
  }
  .brand-name {
    font-size: 24px; font-weight: 700; color: var(--brand-green-dark);
  }
  .contact-details {
    font-size: 19px; font-weight: 500;
  }
  .coupon-band {
    position: absolute;
    left: 0; bottom: 0;
    width: 100%; height: 112px;
    background: var(--brand-green);
    color: #fff;
    text-align: center;
    border-top: 4px solid #dfe9d6;
  }
  .coupon-amount {
    font-family: "Audiowide", sans-serif;
    font-size: 44px; line-height: 50px;
    padding-top: 6px;
  }
  .coupon-offer {
    font-size: 22px; font-weight: 500; line-height: 26px;
  }
  .coupon-note {
    font-size: 12.5px; line-height: 18px;
  }
</style>
</head>
<body>
  <main class="postcard">
    <h1 class="headline">New Construction<br>is on the Rise!</h1>

    <div class="illustration" role="img" aria-label="Illustration of a house under construction: timber roof framework and a partial brick wall set on blueprints, with rolled plans, a pencil, ruler and protractor">
      <div class="illustration-frame"></div>
    </div>

    <svg class="swoosh" viewBox="0 0 556 80" preserveAspectRatio="none" aria-hidden="true">
      <path d="M0 10 Q 230 95 556 0 L556 80 L0 80 Z" fill="#ffffff"/>
      <path d="M0 10 Q 230 95 556 0 L556 14 Q 240 90 0 22 Z" fill="var(--brand-green)"/>
    </svg>

    <p class="tagline">Once the drywall is hung,<br>hidden problems cannot be seen.</p>

    <p class="credentials">Velkor Inspectors are BTW (code) certified and Fully Insured.<br>Protect your clients with a Pre-drywall inspection.</p>

    <div class="contact-row">
      <div class="brand-mark">
        <span class="brand-dot"></span>
        <span class="brand-name">Velkor</span>
      </div>
      <p class="contact-details">555.218.0736 www.the Velkor path.example</p>
    </div>

    <section class="coupon-band">
      <p class="coupon-amount">$25 coupon</p>
      <p class="coupon-offer">for your next Pre-drywall inspection.</p>
      <p class="coupon-note">Mention coupon when booking the Inspection.</p>
    </section>
  </main>
</body>
</html>
```